Modern, Bright Bubble Bath Label

We need a label design for a private label bubble bath we will begin selling.

We will have 8 different scents of bubble bath. Each has a color associated with it as follows: Napa Valley Grape (Purple), Mixed Berry (Blue), Bartlett Pear (Green), Sweet Pineapple (Yellow), Juicy Peach (Orange), Red Raspberry (Red), Creamy Coconut (Brown or White), Kiwi Watermelon (Pink). So what we want is 8 different bottle labels. The labels CAN be different, but they will likely be the same label, just with a different color and different text (scent name).

Labels should be bright, fun, modern, and clean. The main color should be what is listed above, but other colors can be incorporated, as can be seen in the attachments.

Label should be between 2.5" and 3.5" tall, and 7.25" wide. This will be applied to an 8oz boston round, plastic, transparent bottle with a black cap.

For reference, I love The Fern Parlor packaging designs.

Target Market(s)

Women

Industry/Entity Type

Hair And Beauty

Logo Text

Amber Cove

Font styles to use
Serif
Sans Serif

Requirements
Must have
• -Company Logo: 'Amber Cove', which will need to be designed by the winning designer. You can simply put 'Amber Cove' in the label for now as a place holder.
• -Text 'Glimmering Foam Bath'
• -Name of Scent
• -Packaging that is brightly colored and associated with the scent as mentioned in the product description.
• Should be in format that can be edited in Adobe Photoshop. We will add additional text and details (ingredients, description, etc.) in Photoshop once we choose the winning design
Nice to have
• Picture or graphic of associated fruit

```html
<!DOCTYPE html>
<html lang="en">
<head>
<meta charset="utf-8">
<title>Amber Cove – Glimmering Foam Bath Labels</title>
<link rel="stylesheet" href="https://fonts.googleapis.com/css2?family=Roboto+Slab:wght@300;700&display=swap">
<style>
  :root {
    --page: #ffffff;
    --green-dark: #3e8424;
    --green-light: #6cc02f;
    --brown-dark: #5a2d15;
    --brown-light: #d08c5c;
    --orange-dark: #d8720b;
    --orange-light: #fba320;
    --white: #ffffff;
    --cream: #f0d2a8;
    --cocoa: #7a3d1a;
    --nut-dark: #5b2f16;
    --nut-mid: #8a4a24;
    --nut-light: #a85f30;
  }
  * { margin: 0; padding: 0; box-sizing: border-box; }
  html, body {
    width: 1200px;
    height: 942px;
    overflow: hidden;
    background: var(--page);
  }
  .label-set {
    position: relative;
    width: 1200px;
    height: 942px;
    display: flex;
    justify-content: center;
    align-items: center;
    gap: 45px;
  }
  .label {
    position: relative;
    width: 330px;
    height: 590px;
    overflow: hidden;
    font-family: "Roboto Slab", Georgia, serif;
  }
  .label--green  { background: linear-gradient(90deg, var(--green-dark), var(--green-light)); }
  .label--brown  { background: linear-gradient(90deg, var(--brown-dark), var(--brown-light)); }
  .label--orange { background: linear-gradient(90deg, var(--orange-dark), var(--orange-light)); }

  .brand-name {
    position: absolute;
    top: 24px;
    left: 0;
    right: 0;
    text-align: center;
    font-weight: 300;
    font-size: 44px;
    letter-spacing: 1px;
    text-transform: uppercase;
    color: var(--white);
  }
  .product {
    position: absolute;
    top: 118px;
    left: 40px;
    line-height: 1;
  }
  .product__type-bold {
    display: block;
    font-weight: 700;
    font-size: 33px;
    color: var(--white);
  }
  .product__type-light {
    display: block;
    font-weight: 300;
    font-size: 30px;
    color: var(--white);
    margin-top: 2px;
  }
  .product__scent {
    display: block;
    font-weight: 700;
    font-size: 30px;
    line-height: 1.08;
    color: var(--cream);
    margin-top: 8px;
  }
  .label--orange .product__type-bold,
  .label--orange .product__type-light { color: var(--cocoa); }

  .scent-art {
    position: absolute;
    right: -14px;
    bottom: 34px;
    width: 285px;
    height: 300px;
    border-radius: 46% 40% 38% 48% / 44% 42% 46% 46%;
    background: linear-gradient(135deg, var(--nut-light) 0%, var(--nut-mid) 50%, var(--nut-dark) 100%);
  }
</style>
</head>
<body>
  <main class="label-set">
    <section class="label label--green">
      <p class="brand-name">Amber Cove</p>
      <p class="product">
        <span class="product__type-bold">Glimmering</span>
        <span class="product__type-light">Foam Bath</span>
        <span class="product__scent">Creamy<br>Coconut</span>
      </p>
      <div class="scent-art" role="img" aria-label="Faceted low-poly coconut illustration with small bubbles"></div>
    </section>

    <section class="label label--brown">
      <p class="brand-name">Amber Cove</p>
      <p class="product">
        <span class="product__type-bold">Glimmering</span>
        <span class="product__type-light">Foam Bath</span>
        <span class="product__scent">Creamy<br>Coconut</span>
      </p>
      <div class="scent-art" role="img" aria-label="Faceted low-poly coconut illustration with small bubbles"></div>
    </section>

    <section class="label label--orange">
      <p class="brand-name">Amber Cove</p>
      <p class="product">
        <span class="product__type-bold">Glimmering</span>
        <span class="product__type-light">Foam Bath</span>
        <span class="product__scent">Creamy<br>Coconut</span>
      </p>
      <div class="scent-art" role="img" aria-label="Faceted low-poly coconut illustration with small bubbles"></div>
    </section>
  </main>
</body>
</html>
```